依頼詳細
依頼対象ページは「トップページ」と「アクティビティページ」になります。
※ワイヤーフレーム画像を添付いたします。参考にしてください。形状や表示位置等は必ずこの通りにしなければならないというものではありません。お任せいたします。
※利用可能なイメージを添付します。こちらもご利用下さい。

「トップページ」
・「アクティビティ画像群」は鳥沼村の観光スポットを一つずつ画像タイルにして表示させたいと考えています。
・新着情報内の画像は不要です。イメージがあればあてはめて頂いて構いません。
「アクティビティページ」
・「夏の千畳敷」と「投稿一覧」内の画像は不要です。イメージがあればあてはめて頂いて構いません。
・木曽駒ヶ岳だけでなく、その他のアクティビティページにも流用可能なデザインでお願いします。

■その他
・「トップページ」と「アクティビティページ」でヘッダーの大きさを変えて頂いても構いません
・希望色に関してオレンジまたは黒をベースを希望としています。どちらでも構いません。
・SEOを考慮したいのでデザイン内でテキストが可変となりそうな箇所はブラウザ(IE)のデフォルトフォントの使用をお願い致します。
サイトURL
http://www.vill.torinuma-ex.jp/kanko.php
ページ数
2ページ
希望イメージ
シンプル 複雑
単色 カラフル
暗い 明るい
日常 高級
遊び心 厳粛
未来的 伝統的
女性的 男性的
希望する色
オレンジベースまたは黒ベース
納品ファイル
• 高解像度JPG (.jpg)
• イラストレーター形式 (.ai)
補足説明
トップページの画像タイルは大タイル、中タイルの2種類で構成したいと考えています。
季節やイベントの有無によって入れ替えます。
タイル内の「子どもと楽しめるアイコン」「時間アイコン」「インフォメーションエリア」は
様々なアクティビティで共通で利用します。それぞれがの情報が分かりやすい形でデザインをお願いします。
遅くなりすみません。
写真素材は容量が大きいため、添付ではなく以下のURLよりダウンロードしてください。
お手数をお掛けしますが宜しくお願い致します。

■photo1
http://pakkubox-ex.jp/download/a19c3f0b72d84e6a95c1b0d7e3f28a4c6d90b1e2

■photo2
http://pakkubox-ex.jp/download/7c2e90d4b1a83f65e07d9c1b4a2f8e36d5b0c9a7

ワイヤーフレームの「アクティビティ」タイル内に入れる画像はそれぞれ該当する「楓原水産」や「中央アルプス」などを利用してください。
全体的なイメージとして利用するものはお任せいたします。
納品ファイルですがPSD、PNG等の形式でも構いません。
お任せいたします。
素材写真の同じものを下記ミラーサイトに配置しました。
こちらからDLしても構いません。

photo1:
http://survey.kawaridojo-ex.com/photo1.zip

photo2:
http://survey.kawaridojo-ex.com/photo2.zip
・アクティビティページの「カテゴリ」に関して
→すみません。「カテゴリ名」ではなく「アクティビティ名」となります。それぞれのアクティビティを取りまとめるようなカテゴリーの概念はありません。
ミラーサイトのzipファイルが壊れていたので差し替えました。
正常にDL、解凍できることを確認しております。

ご迷惑をおかけしすみませんでした。
締切を1日延ばします。

観光協会のスタッフの皆様にサイトリニューアルのコンセプトをお伝えしたうえで、一次投票、決選投票という手順を踏んで決定いたしました。

この度は多数のご応募ありがとうございました。観光協会の方も大変喜んでおられました。

```html
<!DOCTYPE html>
<html lang="ja">
<head>
<meta charset="utf-8">
<title>信州とりぬま 観光ガイド</title>
<link rel="stylesheet" href="https://fonts.googleapis.com/css2?family=Noto+Sans+JP:wght@400;700&family=Noto+Serif+JP:wght@500;700&display=swap">
<style>
:root{
  --orange:#e8951f;
  --orange-dark:#c9731a;
  --ink:#3b3b3b;
  --sub:#777;
  --paper:#fbf8f1;
  --line:#dcd3c3;
  --green:#6f8f52;
  --sky:#b9cfdc;
  --brown:#5a4a3a;
}
*{box-sizing:border-box;margin:0;padding:0}
html,body{width:741px;height:1200px;overflow:hidden}
body{font-family:"Noto Sans JP",sans-serif;color:var(--ink);font-size:9px;line-height:1.5;
  background:linear-gradient(90deg,#c8ccc4 0,#e9e7df 98px,#e9e7df 643px,#c8ccc4 741px);position:relative}
.side-photos{position:absolute;top:25px;width:98px;height:880px;opacity:.85;
  background:linear-gradient(180deg,#9fb2a0 0,#d5c9ad 25%,#8fa4b4 45%,#c7b69b 65%,#a7b49a 85%,#dcd6c8 100%)}
.side-photos.left{left:0}.side-photos.right{right:0}
.topbar{height:25px;background:#f4f1ea;font-size:7px;color:var(--sub);padding:7px 99px;border-bottom:1px solid var(--line)}
.header{position:absolute;top:25px;left:99px;width:544px;height:50px;background:var(--paper);display:flex;align-items:flex-end;justify-content:space-between;padding:0 10px 8px;border-bottom:3px solid var(--orange)}
.brand{font-family:"Noto Serif JP",serif;font-weight:700;font-size:24px;color:var(--brown);display:flex;align-items:baseline;gap:8px}
.brand small{font-size:14px}
.brand-tag{position:absolute;left:10px;bottom:-3px;background:var(--orange);color:#fff;font-size:7px;padding:0 8px}
.header-link{font-size:10px;color:var(--brown)}
.sidebar{position:absolute;top:75px;left:99px;width:118px}
.about{background:#fff;height:160px;padding:8px;border-right:1px solid var(--line)}
.about h2{font-family:"Noto Serif JP",serif;color:var(--orange-dark);font-size:13px;margin-bottom:4px}
.about p{font-size:7.5px;color:var(--sub);line-height:1.6}
.map{height:115px;background:linear-gradient(160deg,#e6ecd9,#cfdcc1);border-top:1px solid var(--line)}
.side-btn{display:flex;align-items:center;gap:6px;height:40px;margin-top:6px;background:#fff;border:1px solid var(--line);padding:0 8px;font-size:10px;font-weight:700;color:var(--brown)}
.side-btn i{width:12px;height:12px;background:var(--orange);border-radius:50%;display:block}
.side-btn.dark{background:#4a5670;color:#fff;border:0}
.side-btn.dark i{background:#fff}
.hero{position:absolute;top:75px;left:217px;width:426px;height:480px;background:var(--paper)}
.hero-sky{position:absolute;inset:0 0 auto 0;height:275px;background:linear-gradient(180deg,#cfdde6 0,#e7eee7 55%,#f2eddf 100%)}
.hero-copy{position:absolute;top:18px;left:150px;font-family:"Noto Serif JP",serif;font-size:17px;color:#fff;text-shadow:0 0 6px rgba(60,50,30,.6);letter-spacing:2px}
.hero-copy span{display:block;font-size:9px;letter-spacing:1px;margin-top:4px;text-align:right}
.circle{position:absolute;border-radius:50%;border:4px solid #fff;box-shadow:0 2px 6px rgba(0,0,0,.2)}
.c1{left:-8px;top:25px;width:224px;height:224px;background:radial-gradient(circle at 50% 35%,#d9e1d8,#7f9a78 70%,#5f7a5a)}
.c2{left:210px;top:152px;width:110px;height:110px;background:radial-gradient(circle,#c7926a,#6d4630)}
.c3{left:322px;top:152px;width:100px;height:100px;background:radial-gradient(circle at 50% 30%,#dfe7ee,#7d95a6 70%,#56707f)}
.badge{position:absolute;width:44px;height:44px;border-radius:50%;background:var(--orange);color:#fff;text-align:center;font-weight:700;font-size:13px;line-height:1;padding-top:9px;border:2px solid #fff}
.badge small{display:block;font-size:7px;font-weight:400;margin-bottom:2px}
.b1{left:160px;top:212px}
.b2{left:380px;top:222px}
.tile{position:absolute;top:275px;padding:8px 8px}
.tile h3{font-family:"Noto Serif JP",serif;font-size:13px;color:var(--brown);margin-bottom:4px;white-space:nowrap}
.tile h3 small{display:block;font-size:8px;font-weight:500;color:var(--sub)}
.t2 h3,.t3 h3{font-size:11px}
.tile p{font-size:7.5px;color:var(--sub);line-height:1.6}
.tile ul{list-style:none;margin-top:6px;font-size:7px;color:var(--sub)}
.tile li::before{content:"●";color:var(--orange);margin-right:3px}
.t1{left:0;width:204px}.t2{left:210px;width:110px}.t3{left:322px;width:104px}
.spots{position:absolute;top:560px;left:99px;width:544px;height:52px;background:linear-gradient(90deg,#fff,#eef1e6);border:1px solid var(--line);display:flex;align-items:center;justify-content:center;gap:12px}
.spots p{font-size:8px;color:var(--sub)}
.spots strong{font-family:"Noto Serif JP",serif;font-size:15px;color:var(--brown);border-bottom:2px solid var(--orange)}
.news{position:absolute;top:622px;left:110px;width:522px;height:282px;background:#f5efd9;border:1px solid var(--line);padding:10px 14px}
.news h2{font-family:"Noto Serif JP",serif;font-size:13px;color:var(--orange-dark);margin-bottom:6px}
.news h2 span{font-size:8px;color:var(--sub);margin-right:6px}
.news-item{display:flex;gap:10px;background:#fff;height:70px;margin-bottom:8px;padding:6px}
.news-thumb{width:70px;flex:none;background:linear-gradient(135deg,#a9b99a,#6f8760)}
.news-item h3{font-size:9px;color:var(--orange-dark);margin-bottom:3px}
.news-item h3 time{color:var(--sub);font-weight:400;margin-right:6px}
.news-item p{font-size:7px;color:var(--sub)}
.footer{position:absolute;top:912px;left:99px;width:544px;height:263px;background:#fff}
.f-head{display:flex;height:165px;padding:8px}
.f-brand{width:340px}
.f-brand h2{font-family:"Noto Serif JP",serif;font-size:16px;color:var(--brown);margin-bottom:6px}
.thumbs{display:grid;grid-template-columns:repeat(12,1fr);gap:2px}
.thumbs span{height:24px;background:linear-gradient(135deg,#c8b9a2,#8e7f6a)}
.thumbs span:nth-child(3n){background:linear-gradient(135deg,#a9b7c4,#72869a)}
.f-contact{flex:1;padding-left:10px}
.f-photo{height:60px;background:linear-gradient(180deg,#bcd0df,#8fa681);margin-bottom:6px}
.tel{font-size:14px;font-weight:700;color:var(--brown);display:flex;align-items:center;gap:5px}
.f-foot{border-top:2px solid var(--orange);padding:12px 10px;display:flex;justify-content:space-between}
.f-foot h2{font-family:"Noto Serif JP",serif;font-size:16px;color:var(--brown)}
.f-foot p{font-size:8px;color:var(--sub)}
.copyright{position:absolute;bottom:0;left:0;width:741px;height:25px;background:#f4f1ea;text-align:center;font-size:7px;color:var(--sub);padding-top:7px}
</style>
</head>
<body>
<div class="side-photos left" role="img" aria-label="村の風景写真のコラージュ"></div>
<div class="side-photos right" role="img" aria-label="山と花の写真のコラージュ"></div>
<div class="topbar">信州とりぬま観光ガイド｜中央アルプスのふもと鳥沼村の観光情報サイト</div>

<header class="header">
  <div class="brand">信州とりぬま <small>観光ガイド</small></div>
  <span class="brand-tag">中央アルプスの村</span>
  <a class="header-link">鳥沼村観光協会ホームページ</a>
</header>

<aside class="sidebar">
  <div class="about">
    <h2>どんなところ?</h2>
    <p>長野県の南部に位置する鳥沼村は、中央アルプスの雄大な山並みと清らかな水に恵まれた小さな村です。四季折々の自然や祭り、特産品など、ゆったりとした時間をお楽しみください。</p>
  </div>
  <div class="map" role="img" aria-label="鳥沼村の位置を示す地図"></div>
  <div class="side-btn dark"><i></i>公式SNS</div>
  <div class="side-btn"><i></i>くまる情報</div>
  <div class="side-btn"><i></i>お問い合わせ</div>
</aside>

<section class="hero">
  <div class="hero-sky" role="img" aria-label="中央アルプスの山並みと村の風景"></div>
  <p class="hero-copy">豊かな自然と人とのふれあい<span>ゆっくり楽しむ村の旅</span></p>
  <div class="circle c1" role="img" aria-label="楓原水産での釣り体験の様子"></div>
  <div class="circle c2" role="img" aria-label="鳥沼ざおん祭の夜の様子"></div>
  <div class="circle c3" role="img" aria-label="木曽駒ヶ岳の山頂風景"></div>
  <div class="badge b1"><small>所要</small>30分</div>
  <div class="badge b2"><small>所要</small>4時間</div>
  <div class="tile t1">
    <h3>「楓原水産」</h3>
    <p>清流のマス釣りやニジマスのつかみ取りが楽しめます。釣った魚はその場で塩焼きにして味わえます。家族連れにも人気の定番スポットです。</p>
    <ul><li>営業時間 9:00〜17:00</li><li>定休日 水曜日</li><li>駐車場 30台</li></ul>
  </div>
  <div class="tile t2">
    <h3>「鳥沼ざおん祭」</h3>
    <p>夏の夜を彩る村の伝統行事。みこしと花火で村じゅうがにぎわいます。</p>
    <ul><li>8月上旬 開催</li><li>会場 村中心部</li></ul>
  </div>
  <div class="tile t3">
    <h3>「木曽駒ヶ岳」<small>中央アルプス</small></h3>
    <p>ロープウェイで標高2,600mへ。高山植物と絶景が広がります。</p>
    <ul><li>通年 運行</li><li>ロープウェイ利用</li></ul>
  </div>
</section>

<section class="spots">
  <p>信州とりぬま まるごと楽しもう</p>
  <strong>おすすめの観光スポット一覧</strong>
</section>

<section class="news">
  <h2><span>最新</span>お知らせ</h2>
  <article class="news-item">
    <div class="news-thumb" role="img" aria-label="新緑の山の写真"></div>
    <div><h3><time>2013.05.20</time>新緑の季節のご案内</h3><p>村内の散策路が見ごろを迎えています。おすすめコースと休憩所をご紹介します。ぜひお出かけください。</p></div>
  </article>
  <article class="news-item">
    <div class="news-thumb" role="img" aria-label="イベント会場の写真"></div>
    <div><h3><time>2013.05.12</time>観光協会の営業時間変更について</h3><p>6月より土日の窓口営業時間が変わります。詳しくは観光協会までお問い合わせください。</p></div>
  </article>
  <article class="news-item">
    <div class="news-thumb" role="img" aria-label="ウォーキングイベントの写真"></div>
    <div><h3><time>2013.05.01</time>【参加者募集】村めぐりウォーキング</h3><p>地元ガイドと歩く春のウォーキングを開催します。参加無料、定員30名です。</p></div>
  </article>
</section>

<footer class="footer">
  <div class="f-head">
    <div class="f-brand">
      <h2>信州 とりぬま</h2>
      <div class="thumbs" role="img" aria-label="村の観光写真のサムネイル一覧">
        <span></span><span></span><span></span><span></span><span></span><span></span><span></span><span></span><span></span><span></span><span></span><span></span>
        <span></span><span></span><span></span><span></span><span></span><span></span><span></span><span></span><span></span><span></span><span></span><span></span>
        <span></span><span></span><span></span><span></span><span></span><span></span><span></span><span></span><span></span><span></span><span></span><span></span>
        <span></span><span></span><span></span><span></span><span></span><span></span><span></span><span></span><span></span><span></span><span></span><span></span>
      </div>
    </div>
    <div class="f-contact">
      <div class="f-photo" role="img" aria-label="観光協会の建物の写真"></div>
      <p class="tel"><svg width="12" height="12" viewBox="0 0 24 24"><path fill="#e8951f" d="M6.6 10.8a15 15 0 006.6 6.6l2.2-2.2a1 1 0 011-.25 11.4 11.4 0 003.6.6 1 1 0 011 1V20a1 1 0 01-1 1A17 17 0 013 4a1 1 0 011-1h3.5a1 1 0 011 1 11.4 11.4 0 00.6 3.6 1 1 0 01-.25 1z"/></svg>TEL. 0265-00-4821</p>
      <p class="tel">FAX. 0265-00-4822</p>
      <p style="font-size:7px;color:var(--sub)">受付 8:30〜17:15（土日祝を除く）</p>
    </div>
  </div>
  <div class="f-foot">
    <h2>鳥沼村観光協会</h2>
    <p>〒399-0000 長野県上伊那郡鳥沼村0000番地</p>
  </div>
</footer>

<div class="copyright">Copyright © 鳥沼村観光協会 All Rights Reserved.</div>
</body>
</html>
```